Construction Business Card Design

We have a landscape construction company based in Australia
Were out of business cards ,
So now we're after a fresh looking modern card to give a fresh look to our business ....
We would like the business card to have the
(Front)
Tallow Ridge Pty Ltd
Director Gordon Marsh
0412563908
(Back)
Landscape,Construction,Paving,Excavation
(In smaller font low in the frame of card)
Different textures , curved edge , vertical and horizontal designs also minimal colours per design
Eg one side black , one coloured or a splash here or there
Industry/Entity Type
Landscape
Contact Information for Business Card
Tallow Ridge Pty Ltd
Director Gordon Marsh
0412563908
Landscape,Paving,Construction,Excavation

```html
<!DOCTYPE html>
<html lang="en">
<head>
<meta charset="utf-8">
<title>Tallow Ridge Pty Ltd – Business Card</title>
<link rel="stylesheet" href="https://fonts.googleapis.com/css2?family=Didact+Gothic&family=Mulish:wght@700&display=swap">
<style>
  :root {
    --backdrop: #b9b9b9;
    --card-dark: #262626;
    --accent-orange: #f7901e;
    --text-white: #ffffff;
    --card-width: 425px;
    --card-height: 750px;
    --band-width: 25px;
    --corner-radius: 64px;
  }
  * { margin: 0; padding: 0; box-sizing: border-box; }
  html, body {
    width: 1200px;
    height: 1000px;
    overflow: hidden;
  }
  body {
    background: radial-gradient(ellipse at center, #d6d6d6 0%, var(--backdrop) 55%, #9a9a9a 100%);
    position: relative;
  }
  .card {
    position: absolute;
    top: 120px;
    width: var(--card-width);
    height: var(--card-height);
    background: var(--card-dark);
    box-shadow: 0 6px 18px rgba(0, 0, 0, 0.35);
    overflow: hidden;
  }
  .card-band {
    position: absolute;
    top: 0;
    bottom: 0;
    width: var(--band-width);
    background: var(--accent-orange);
  }
  /* Front side */
  .card--front {
    left: 120px;
    border-bottom-left-radius: var(--corner-radius);
  }
  .card--front .card-band { right: 0; }
  .company-name {
    position: absolute;
    left: 38px;
    top: 36px;
    font-family: "Mulish", sans-serif;
    font-weight: 700;
    font-size: 27px;
    color: var(--text-white);
    letter-spacing: 0.2px;
  }
  .contact {
    position: absolute;
    left: 38px;
    top: 88px;
    font-family: "Didact Gothic", sans-serif;
    font-size: 20px;
    line-height: 23px;
    color: var(--accent-orange);
  }
  /* Back side */
  .card--back {
    left: 655px;
    border-bottom-right-radius: var(--corner-radius);
  }
  .card--back .card-band { left: 0; }
  .services {
    position: absolute;
    left: 48px;
    top: 30px;
    list-style: none;
    font-family: "Didact Gothic", sans-serif;
    font-size: 24px;
    line-height: 33px;
    color: var(--accent-orange);
    letter-spacing: 0.3px;
  }
</style>
</head>
<body>
  <section class="card card--front" aria-label="Card front">
    <h1 class="company-name">Tallow Ridge Pty Ltd</h1>
    <p class="contact">
      <span class="contact-role">Director Gordon Marsh</span><br>
      <span class="contact-phone">0412563908</span>
    </p>
    <div class="card-band"></div>
  </section>

  <section class="card card--back" aria-label="Card back">
    <div class="card-band"></div>
    <ul class="services">
      <li>Landscape</li>
      <li>Paving</li>
      <li>Construction</li>
      <li>Excavation</li>
    </ul>
  </section>
</body>
</html>
```